Health care technology software systems

We have a solid logo. We have company colors that will need to be used as well. We just need a great business card design. We sell to health plans but want to be modern
Updates

Need extra days to review

Target Market(s)

Health technology sector selling into Health Plans

Industry/Entity Type

Health Care Technology

Contact Information for Business Card

Name, title, address, phone number, email

Requirements
Must have
• Use of Kembrata corporate colors - Uploaded w/ our logos

```html
<!DOCTYPE html>
<html lang="en">
<head>
<meta charset="utf-8">
<title>Kembrata Business Card</title>
<link rel="stylesheet" href="https://fonts.googleapis.com/css2?family=Montserrat:wght@300;400;700&display=swap">
<style>
  :root {
    --page-bg: #ececef;
    --card-white: #ffffff;
    --lavender: #e2e4f3;
    --ice: #eaf2fb;
    --ink: #3a3a3c;
    --brand-blue: #1ba1e2;
    --rule: #b9bcc8;
  }
  * { box-sizing: border-box; margin: 0; padding: 0; }
  html, body {
    width: 1200px; height: 900px; overflow: hidden;
    background: var(--page-bg);
    font-family: "Montserrat", sans-serif;
    color: var(--ink);
  }
  .card {
    position: absolute;
    width: 700px; height: 400px;
    left: 250px;
    background: var(--card-white);
    overflow: hidden;
  }
  .card--front {
    top: 40px;
    background:
      radial-gradient(ellipse 240px 220px at 540px 205px, #ffffff 0%, #ffffff 55%, rgba(255,255,255,0) 100%),
      linear-gradient(110deg, #ffffff 0%, #f1f2f9 45%, var(--lavender) 80%, var(--ice) 100%);
  }
  .card--back { top: 460px; }

  .wordmark {
    position: absolute;
    display: flex; align-items: center;
    font-weight: 300;
    color: var(--ink);
    letter-spacing: 0.5px;
    line-height: 1;
  }
  .wordmark__dot {
    border-radius: 50%;
    background: var(--brand-blue);
    flex: none;
  }
  .card--front .wordmark { left: 53px; top: 270px; font-size: 46px; gap: 18px; }
  .card--front .wordmark__dot { width: 40px; height: 40px; }
  .card--back .wordmark { left: 152px; top: 236px; font-size: 80px; gap: 28px; }
  .card--back .wordmark__dot { width: 68px; height: 68px; }

  .contact { position: absolute; left: 400px; top: 92px; }
  .contact__name { font-weight: 700; font-size: 22px; line-height: 1.05; }
  .contact__role { font-weight: 400; font-size: 19px; color: var(--brand-blue); line-height: 1.15; }
  .contact__address { margin-top: 20px; font-size: 15px; line-height: 20px; }
  .contact__list { list-style: none; margin-top: 16px; font-size: 15px; }
  .contact__item { display: flex; align-items: center; gap: 10px; height: 25px; }
  .contact__item--web { margin-top: 18px; }
  .contact__icon { width: 16px; height: 16px; flex: none; }

  .base-rule {
    position: absolute; left: 152px; top: 349px;
    width: 548px; height: 2px;
    background: var(--rule);
  }
</style>
</head>
<body>

<section class="card card--front">
  <div class="wordmark"><span class="wordmark__dot"></span><span class="wordmark__name">kembrata</span></div>

  <div class="contact">
    <p class="contact__name">Dana Kessler</p>
    <p class="contact__role">co-founder</p>
    <p class="contact__address">2450 ALDER ROW 210<br>Millbrook, Oregon 97000, US</p>
    <ul class="contact__list">
      <li class="contact__item">
        <svg class="contact__icon" viewBox="0 0 24 24"><path fill="var(--brand-blue)" d="M6.6 10.8a15.1 15.1 0 0 0 6.6 6.6l2.2-2.2a1 1 0 0 1 1-.25 11.4 11.4 0 0 0 3.6.57 1 1 0 0 1 1 1V20a1 1 0 0 1-1 1A17 17 0 0 1 3 4a1 1 0 0 1 1-1h3.5a1 1 0 0 1 1 1c0 1.25.2 2.45.57 3.57a1 1 0 0 1-.25 1z"/></svg>
        <span>0745-908-312</span>
      </li>
      <li class="contact__item">
        <svg class="contact__icon" viewBox="0 0 24 24"><rect x="2" y="5" width="20" height="14" fill="var(--brand-blue)"/><path d="M2 5l10 8 10-8M2 19l7-7M22 19l-7-7" stroke="#fff" stroke-width="1.6" fill="none"/></svg>
        <span>kembrata@mail.com</span>
      </li>
      <li class="contact__item contact__item--web">
        <svg class="contact__icon" viewBox="0 0 24 24" fill="none" stroke="var(--brand-blue)" stroke-width="1.5"><circle cx="12" cy="12" r="9.5"/><ellipse cx="12" cy="12" rx="4.2" ry="9.5"/><path d="M2.5 12h19M4 7h16M4 17h16"/></svg>
        <span>kembrata.com</span>
      </li>
    </ul>
  </div>
</section>

<section class="card card--back">
  <div class="wordmark"><span class="wordmark__dot"></span><span class="wordmark__name">kembrata</span></div>
  <div class="base-rule" aria-hidden="true"></div>
</section>

</body>
</html>
```